Criação de Papelaria (6 itens) para Automotivo
" Somos uma loja compacta e o nosso diferencial é o bom atendimento personalizado que damos ao cliente, e que a maioria elogia. Compramos, vendemos, trocamos e aceitamos carros consignados. "

```html
<!DOCTYPE html>
<html lang="pt-BR">
<head>
<meta charset="utf-8">
<title>Brilho Veículos — Cartão de Visita</title>
<link rel="stylesheet" href="https://fonts.googleapis.com/css2?family=Exo+2:wght@400;600;800&display=swap">
<style>
  :root {
    --page-bg: #e6e6e4;
    --card-dark: #1a1a1a;
    --card-darker: #0e0e0e;
    --brand-orange: #f08a1c;
    --text-light: #e9e9e9;
    --text-muted: #c9c9c9;
    --icon-fill: #e5701a;
    --band-light: #f2f2f2;
    --band-dark: #2a2a2a;
  }
  * { margin: 0; padding: 0; box-sizing: border-box; }
  html, body {
    width: 1200px; height: 1200px; overflow: hidden;
    background: var(--page-bg);
    font-family: "Exo 2", sans-serif;
  }
  .canvas { position: relative; width: 1200px; height: 1200px; }
  .card {
    position: absolute; left: 150px; width: 900px; height: 500px;
    border-radius: 6px; overflow: hidden;
    background: radial-gradient(ellipse at 40% 40%, var(--card-dark), var(--card-darker));
    box-shadow: 0 10px 30px rgba(0,0,0,.25);
  }
  .card--info { top: 80px; }
  .card--brand { top: 620px; }

  .mascot-area {
    position: absolute; left: 40px; top: 50px; width: 270px; height: 400px;
    border-radius: 120px 120px 30px 30px;
    background: radial-gradient(circle at 50% 35%, #d9d4c6 0%, #8a8478 45%, #3b3a37 80%, transparent 100%);
    opacity: .9;
  }
  .finish-band {
    position: absolute; left: 0; bottom: 0; width: 900px; height: 150px;
  }

  .brand-name {
    position: absolute; color: var(--brand-orange);
    font-weight: 800; text-transform: uppercase; line-height: .95;
  }
  .card--info .brand-name { left: 370px; top: 70px; font-size: 46px; }

  .contact-list {
    position: absolute; left: 370px; top: 190px; list-style: none;
    color: var(--text-light); font-size: 22px; font-weight: 400;
  }
  .contact-item { display: flex; align-items: center; gap: 16px; margin-bottom: 14px; }
  .contact-icon {
    width: 30px; height: 30px; border-radius: 5px; background: var(--icon-fill);
    display: flex; align-items: center; justify-content: center; flex: none;
  }

  .card--brand .brand-block {
    position: absolute; left: 0; right: 0; top: 140px; text-align: center;
  }
  .card--brand .brand-name {
    position: static; font-size: 104px; letter-spacing: 2px;
  }
  .tagline {
    margin-top: 22px; color: var(--text-light);
    font-size: 40px; font-weight: 400; letter-spacing: 1px;
  }
</style>
</head>
<body>
<main class="canvas">

  <section class="card card--info">
    <div class="mascot-area" role="img" aria-label="Mascote ilustrado da loja segurando uma chave de carro"></div>

    <svg class="finish-band" viewBox="0 0 900 150" role="img" aria-label="Faixa quadriculada de bandeira de chegada">
      <defs>
        <linearGradient id="band-tone" x1="0" x2="1">
          <stop offset="0" stop-color="var(--band-light)"/>
          <stop offset=".5" stop-color="#9a9a9a"/>
          <stop offset="1" stop-color="var(--band-light)"/>
        </linearGradient>
      </defs>
      <path d="M0 130 C 250 120, 550 90, 900 10 L 900 50 C 560 130, 260 150, 0 150 Z" fill="url(#band-tone)" opacity=".85"/>
    </svg>

    <div class="brand-name">Brilho<br>Veículos</div>

    <ul class="contact-list">
      <li class="contact-item">
        <span class="contact-icon">
          <svg width="18" height="18" viewBox="0 0 24 24"><path fill="#fff" d="M6.6 10.8a15 15 0 0 0 6.6 6.6l2.2-2.2c.3-.3.7-.4 1-.2 1.1.4 2.3.6 3.6.6.6 0 1 .4 1 1V20c0 .6-.4 1-1 1A17 17 0 0 1 3 4c0-.6.4-1 1-1h3.5c.6 0 1 .4 1 1 0 1.3.2 2.5.6 3.6.1.3 0 .7-.2 1z"/></svg>
        </span>
        (00) 0000-0000
      </li>
      <li class="contact-item">
        <span class="contact-icon">
          <svg width="18" height="18" viewBox="0 0 24 24"><rect x="3" y="6" width="18" height="12" rx="1" fill="none" stroke="#fff" stroke-width="2"/><path d="M3 7l9 6 9-6" fill="none" stroke="#fff" stroke-width="2"/></svg>
        </span>
        contato@exemplo.com.br
      </li>
      <li class="contact-item">
        <span class="contact-icon">
          <svg width="18" height="18" viewBox="0 0 24 24"><path fill="#fff" d="M12 2a7 7 0 0 0-7 7c0 5 7 13 7 13s7-8 7-13a7 7 0 0 0-7-7zm0 9.5A2.5 2.5 0 1 1 12 6a2.5 2.5 0 0 1 0 5.5z"/></svg>
        </span>
        Rua exemplo, 000
      </li>
      <li class="contact-item">
        <span class="contact-icon">
          <svg width="18" height="18" viewBox="0 0 24 24"><path d="M5 12l5 5 9-10" fill="none" stroke="#fff" stroke-width="3"/></svg>
        </span>
        Cidade-UF, CEP: 0000-000
      </li>
    </ul>
  </section>

  <section class="card card--brand">
    <div class="brand-block">
      <div class="brand-name">Brilho Veículos</div>
      <p class="tagline">A sua melhor opção</p>
    </div>
  </section>

</main>
</body>
</html>
```